WebApp for IoT (Glim lights and Tarvo/Mellobin)

I am going to create my own dashbord for Quillon Pro (See other examples on https://quillondeck.io/) But I want it much more flexible and advanced.
One page per room (So I can have an Tabrix in each room with all functions just for that room) and include controls for light (both overall for the room and in an popupwindow all lightbulbs n the room - se more about how its done in Varnell Glim app on https://www.varnell-glim.com/en-us/explore-glim/apps/bridge) aswell as set volume/track for Tarvo.

I want the final solution to be "skinable" so I can choose from Blue-CSS to Green-CSS etc, but at this moment I only want ONE color!

I have added an PDF with the functions I am thinking of, but the design is for you to create!

Please have in mind it will be running on Tabrixes on the wall, and in the mobile.

For the moment I only want an PSD of the "Room page", "Light popup" and "Sound Popup", but I might contract the winner to get HTML/CSS as second step.

```html
<!DOCTYPE html>
<html lang="en">
<head>
<meta charset="utf-8">
<title>Room Dashboard – Room page, Light popup, Sound popup</title>
<link href="https://fonts.googleapis.com/css2?family=Inter:wght@400;500;600;700&display=swap" rel="stylesheet">
<style>
:root{
  --canvas:#e6e6e8;
  --header:#27272a;
  --tile:#222224;
  --tile-line:#3a3a3e;
  --popup:#1e1e20;
  --blue-1:#3478ff;
  --blue-2:#1d4fe6;
  --blue-deep:#1c2f7a;
  --text:#ffffff;
  --text-soft:#c9d4ff;
  --toggle-off:#101012;
  --dim:rgba(46,46,50,.62);
}
*{box-sizing:border-box;margin:0;padding:0}
html,body{width:1200px;height:940px;overflow:hidden}
body{background:var(--canvas);font-family:"Inter",Arial,sans-serif;color:var(--text);position:relative}
.screen{position:absolute;width:570px;height:428px;overflow:hidden}
.screen--kitchen{background:linear-gradient(160deg,#5b6660 0%,#4a4f4c 40%,#585656 70%,#4b4a4b 100%)}
.screen--bedroom{background:linear-gradient(170deg,#4a4f5e 0%,#3f4452 45%,#4d5160 75%,#3c3f48 100%)}
.room-backdrop{position:absolute;inset:0}
.header{position:absolute;left:0;top:0;width:570px;height:58px;background:var(--header);border-radius:0 0 10px 10px}
.room{position:absolute;left:8px;top:19px;display:flex;align-items:center;gap:8px;font-weight:600;font-size:11.5px}
.room svg{display:block}
.temp{position:absolute;left:258px;top:16px;font-size:20px;font-weight:400;display:flex;align-items:flex-start;gap:2px}
.temp sup{font-size:10px;margin-top:-3px}
.temp svg{margin-left:6px;margin-top:3px}
.date{position:absolute;left:436px;top:17px;display:flex;align-items:center;gap:6px}
.date .day{font-size:20px;padding-right:7px;border-right:1.5px solid var(--blue-1);line-height:20px}
.date .month{font-size:8.5px;line-height:10px}
.time{position:absolute;left:531px;top:21px;width:44px;height:17px;background:#333337;border-radius:5px;font-size:8.5px;padding:3px 0 0 8px}
.greeting{position:absolute;left:0;width:570px;text-align:center;font-size:20px;font-weight:400}
.greeting b{font-weight:700}

.control{position:absolute;width:169px;height:56px;border-radius:6px;background:var(--tile)}
.control--on{background:linear-gradient(90deg,var(--blue-1),var(--blue-2))}
.control .icon{position:absolute;left:12px;top:17px}
.control .title{position:absolute;left:43px;top:14px;font-size:11px;font-weight:600}
.control .sub{position:absolute;left:43px;top:31px;font-size:7.5px;color:var(--text-soft)}
.control:not(.control--on) .sub{color:#c6c6c6}
.pill{position:absolute;right:13px;top:21px;width:34px;height:16px;border-radius:8px;background:rgba(20,40,140,.55);font-size:8px;display:flex;align-items:center}
.pill .knob{position:absolute;top:2px;width:12px;height:12px;border-radius:50%;background:#fff}
.pill--on span{padding-left:6px}
.pill--on .knob{right:2px}
.pill--off{background:#161618}
.pill--off .knob{left:2px}
.pill--off span{padding-left:17px;color:#bbb}

.slider{position:absolute;width:28px;height:68px;border-radius:14px;background:var(--blue-deep);overflow:hidden;box-shadow:0 3px 8px rgba(0,0,0,.3)}
.slider .fill{position:absolute;left:0;right:0;bottom:0;background:linear-gradient(180deg,#6f99ff,#3b6df2)}
.slider .badge{position:absolute;left:3px;top:8px;width:22px;height:9px;border-radius:5px;background:#121632;font-size:4.5px;text-align:center;line-height:9px}
.slider svg{position:absolute;left:8px;bottom:7px}

.device{position:absolute;width:71px;height:85px;border-radius:6px;background:var(--tile)}
.device--on{background:linear-gradient(180deg,var(--blue-1),var(--blue-2))}
.device svg{position:absolute;left:29px;top:10px}
.device .label{position:absolute;top:32px;width:100%;text-align:center;font-size:8.8px}
.device .rule{position:absolute;left:4px;right:4px;top:55px;height:1px;background:var(--tile-line)}
.device--on .rule{background:rgba(255,255,255,.18)}
.switch{position:absolute;left:20px;top:65px;width:30px;height:13px;border-radius:7px;background:var(--toggle-off)}
.switch .knob{position:absolute;top:2px;left:3px;width:10px;height:10px;border-radius:50%;background:#fff}
.device--on .switch{background:var(--blue-deep)}
.device--on .switch .knob{left:17px}

.dim{position:absolute;inset:0;background:var(--dim)}
.cursor{position:absolute}

.popup{position:absolute;background:var(--popup);border:1px solid #3c3c40;border-radius:18px;box-shadow:0 10px 30px rgba(0,0,0,.35)}
.popup h2{position:absolute;font-size:14px;font-weight:700}
.scene{position:absolute;width:86px;height:92px;border-radius:7px;background:#161617;border:1px solid #2e2e31}
.scene .orb{position:absolute;left:25px;top:13px;width:35px;height:35px;border-radius:50%}
.scene .name{position:absolute;top:58px;width:100%;text-align:center;font-size:11.5px}
.orb--tropical{background:linear-gradient(180deg,#ffb08a,#e8fbff 55%,#9ff3ff)}
.orb--sunrise{background:linear-gradient(180deg,#ffb35a,#ff6a3d)}
.orb--concentrate{background:linear-gradient(180deg,#8fd3d8,#1a5e70 55%,#0c2e3e)}
.orb--dimmed{background:linear-gradient(180deg,#22b36e,#148a55 55%,#0b3d2a)}
.orb--night{background:linear-gradient(180deg,#8d4ba0,#5a2a8a 55%,#3a1a6a)}
.select{position:absolute;left:23px;top:46px;width:282px;height:40px;border-radius:10px;border:1px solid #4a4a4e;background:#19191b;display:flex;align-items:center;padding-left:13px;font-size:12px;gap:9px}
.select .ring{width:10px;height:10px;border-radius:50%;border:1.5px solid #fff}
.select svg{position:absolute;right:28px;top:17px}
</style>
</head>
<body>

<!-- Kitchen room page -->
<section class="screen screen--kitchen" style="left:21px;top:23px">
  <div class="room-backdrop" role="img" aria-label="Blurred photo of the kitchen"></div>
  <header class="header">
    <div class="room"><svg width="10" height="13" viewBox="0 0 10 13" fill="#fff"><rect x="0" y="0" width="1.2" height="5"/><rect x="2.2" y="0" width="1.2" height="5"/><rect x="4.4" y="0" width="1.2" height="5"/><rect x="0" y="4" width="5.6" height="2" rx="1"/><rect x="2" y="5" width="1.6" height="8"/><path d="M7 0c2 0 2.6 3 2.6 6H8.6v7H7z"/></svg>Kitchen<svg width="9" height="5" viewBox="0 0 9 5"><path d="M0 0h9L4.5 5z" fill="#fff"/></svg></div>
    <div class="temp">23<sup>°</sup><svg width="17" height="17" viewBox="0 0 24 24" fill="none" stroke="#fff" stroke-width="1.8"><circle cx="12" cy="12" r="5"/><path d="M12 1v3M12 20v3M1 12h3M20 12h3M4.2 4.2l2.1 2.1M17.7 17.7l2.1 2.1M4.2 19.8l2.1-2.1M17.7 6.3l2.1-2.1"/></svg></div>
    <div class="date"><svg width="17" height="17" viewBox="0 0 24 24" fill="none" stroke="#fff" stroke-width="1.5"><rect x="2" y="4" width="18" height="17" rx="2"/><path d="M2 9h18M7 2v4M15 2v4"/><circle cx="18" cy="18" r="4" fill="#27272a"/><path d="M18 16v2h1.5"/></svg><span class="day">14</span><span class="month">July<br>2022</span></div>
    <div class="time">15:23</div>
  </header>
  <h1 class="greeting" style="top:84px"><b>Good morning</b>, today is Friday</h1>

  <div class="control control--on" style="left:26px;top:151px">
    <svg class="icon" width="22" height="22" viewBox="0 0 24 24" fill="none" stroke="#fff" stroke-width="1.8"><circle cx="12" cy="12" r="5" fill="#fff"/><path d="M12 1v3M12 20v3M1 12h3M20 12h3M4.2 4.2l2.1 2.1M17.7 17.7l2.1 2.1M4.2 19.8l2.1-2.1M17.7 6.3l2.1-2.1"/></svg>
    <span class="title">Light</span><span class="sub">Lorem Ipsum</span>
    <div class="pill pill--on"><span>on</span><i class="knob"></i></div>
  </div>
  <div class="slider" style="left:201px;top:145px"><div class="fill" style="height:55%"></div><div class="badge">52%</div><svg width="12" height="12" viewBox="0 0 24 24" fill="none" stroke="#fff" stroke-width="2"><circle cx="12" cy="12" r="4.5"/><path d="M12 1v3M12 20v3M1 12h3M20 12h3M4.2 4.2l2.1 2.1M17.7 17.7l2.1 2.1M4.2 19.8l2.1-2.1M17.7 6.3l2.1-2.1"/></svg></div>
  <svg class="cursor" style="left:172px;top:180px" width="10" height="13" viewBox="0 0 10 13"><path d="M3 1v6L1.5 6C.5 6 .3 7 1 7.7L4 12h5V6.5L5 5.7V1c0-1-2-1-2 0z" fill="#fff" stroke="#000" stroke-width=".6"/></svg>

  <div class="device device--on" style="left:394px;top:151px"><svg width="12" height="15" viewBox="0 0 12 15" fill="#fff"><path d="M6 0a5 5 0 0 0-3 9v2h6V9A5 5 0 0 0 6 0z"/><rect x="3.5" y="12" width="5" height="1.4" rx=".7"/></svg><span class="label">Bulb 01</span><i class="rule"></i><div class="switch"><i class="knob"></i></div></div>
  <div class="device" style="left:472px;top:151px"><svg width="12" height="15" viewBox="0 0 12 15" fill="#fff"><path d="M6 0a5 5 0 0 0-3 9v2h6V9A5 5 0 0 0 6 0z"/><rect x="3.5" y="12" width="5" height="1.4" rx=".7"/></svg><span class="label">Bulb 02</span><i class="rule"></i><div class="switch"><i class="knob"></i></div></div>
  <div class="device" style="left:394px;top:244px"><svg width="12" height="15" viewBox="0 0 12 15" fill="#fff"><path d="M6 0a5 5 0 0 0-3 9v2h6V9A5 5 0 0 0 6 0z"/><rect x="3.5" y="12" width="5" height="1.4" rx=".7"/></svg><span class="label">Bulb 03</span><i class="rule"></i><div class="switch"><i class="knob"></i></div></div>
  <div class="device" style="left:472px;top:244px"><svg width="12" height="15" viewBox="0 0 12 15" fill="#fff"><path d="M6 0a5 5 0 0 0-3 9v2h6V9A5 5 0 0 0 6 0z"/><rect x="3.5" y="12" width="5" height="1.4" rx=".7"/></svg><span class="label">Bulb 04</span><i class="rule"></i><div class="switch"><i class="knob"></i></div></div>
</section>

<!-- Kitchen light popup -->
<section class="screen screen--kitchen" style="left:610px;top:23px">
  <div class="room-backdrop" role="img" aria-label="Blurred photo of the kitchen"></div>
  <header class="header">
    <div class="room"><svg width="10" height="13" viewBox="0 0 10 13" fill="#fff"><rect x="0" y="0" width="1.2" height="5"/><rect x="2.2" y="0" width="1.2" height="5"/><rect x="4.4" y="0" width="1.2" height="5"/><rect x="0" y="4" width="5.6" height="2" rx="1"/><rect x="2" y="5" width="1.6" height="8"/><path d="M7 0c2 0 2.6 3 2.6 6H8.6v7H7z"/></svg>Kitchen<svg width="9" height="5" viewBox="0 0 9 5"><path d="M0 0h9L4.5 5z" fill="#fff"/></svg></div>
    <div class="temp">23<sup>°</sup><svg width="17" height="17" viewBox="0 0 24 24" fill="none" stroke="#fff" stroke-width="1.8"><circle cx="12" cy="12" r="5"/><path d="M12 1v3M12 20v3M1 12h3M20 12h3M4.2 4.2l2.1 2.1M17.7 17.7l2.1 2.1M4.2 19.8l2.1-2.1M17.7 6.3l2.1-2.1"/></svg></div>
    <div class="date"><svg width="17" height="17" viewBox="0 0 24 24" fill="none" stroke="#fff" stroke-width="1.5"><rect x="2" y="4" width="18" height="17" rx="2"/><path d="M2 9h18M7 2v4M15 2v4"/><circle cx="18" cy="18" r="4" fill="#27272a"/><path d="M18 16v2h1.5"/></svg><span class="day">14</span><span class="month">July<br>2022</span></div>
    <div class="time">15:23</div>
  </header>
  <h1 class="greeting" style="top:84px"><b>Good morning</b>, today is Friday</h1>
  <div class="device" style="left:472px;top:151px"><svg width="12" height="15" viewBox="0 0 12 15" fill="#fff"><path d="M6 0a5 5 0 0 0-3 9v2h6V9A5 5 0 0 0 6 0z"/><rect x="3.5" y="12" width="5" height="1.4" rx=".7"/></svg><span class="label">Bulb 02</span><i class="rule"></i><div class="switch"><i class="knob"></i></div></div>
  <div class="device" style="left:394px;top:244px"><svg width="12" height="15" viewBox="0 0 12 15" fill="#fff"><path d="M6 0a5 5 0 0 0-3 9v2h6V9A5 5 0 0 0 6 0z"/><rect x="3.5" y="12" width="5" height="1.4" rx=".7"/></svg><span class="label">Bulb 03</span><i class="rule"></i><div class="switch"><i class="knob"></i></div></div>
  <div class="device" style="left:472px;top:244px"><svg width="12" height="15" viewBox="0 0 12 15" fill="#fff"><path d="M6 0a5 5 0 0 0-3 9v2h6V9A5 5 0 0 0 6 0z"/><rect x="3.5" y="12" width="5" height="1.4" rx=".7"/></svg><span class="label">Bulb 04</span><i class="rule"></i><div class="switch"><i class="knob"></i></div></div>
  <div class="dim"></div>

  <div class="device device--on" style="left:394px;top:151px"><svg width="12" height="15" viewBox="0 0 12 15" fill="#fff"><path d="M6 0a5 5 0 0 0-3 9v2h6V9A5 5 0 0 0 6 0z"/><rect x="3.5" y="12" width="5" height="1.4" rx=".7"/></svg><span class="label">Bulb 01</span><i class="rule"></i><div class="switch"><i class="knob"></i></div></div>
  <svg class="cursor" style="left:437px;top:225px" width="10" height="13" viewBox="0 0 10 13"><path d="M3 1v6L1.5 6C.5 6 .3 7 1 7.7L4 12h5V6.5L5 5.7V1c0-1-2-1-2 0z" fill="#fff" stroke="#000" stroke-width=".6"/></svg>

  <div class="popup" style="left:23px;top:110px;width:359px;height:267px">
    <h2 style="left:32px;top:27px">Light 01</h2>
    <div class="scene" style="left:32px;top:61px"><i class="orb orb--tropical"></i><span class="name">Tropical</span></div>
    <div class="scene" style="left:127px;top:61px"><i class="orb orb--sunrise"></i><span class="name">Sunrise</span></div>
    <div class="scene" style="left:221px;top:61px"><i class="orb orb--concentrate"></i><span class="name">Concentrate</span></div>
    <div class="scene" style="left:32px;top:160px"><i class="orb orb--dimmed"></i><span class="name">Dimmed</span></div>
    <div class="scene" style="left:127px;top:160px"><i class="orb orb--night"></i><span class="name">Night</span></div>
  </div>
</section>

<!-- Bedroom room page -->
<section class="screen screen--bedroom" style="left:21px;top:471px">
  <div class="room-backdrop" role="img" aria-label="Blurred photo of the bedroom with a bed"></div>
  <header class="header">
    <div class="room"><svg width="15" height="11" viewBox="0 0 15 11" fill="#fff"><rect x="1.5" y="0" width="12" height="5" rx="1"/><rect x="0" y="5" width="15" height="4" rx="1"/><rect x="0.5" y="9" width="1.5" height="2"/><rect x="13" y="9" width="1.5" height="2"/></svg>Bedroom<svg width="9" height="5" viewBox="0 0 9 5"><path d="M0 0h9L4.5 5z" fill="#fff"/></svg></div>
    <div class="temp">23<sup>°</sup><svg width="17" height="17" viewBox="0 0 24 24" fill="none" stroke="#fff" stroke-width="1.8"><circle cx="12" cy="12" r="5"/><path d="M12 1v3M12 20v3M1 12h3M20 12h3M4.2 4.2l2.1 2.1M17.7 17.7l2.1 2.1M4.2 19.8l2.1-2.1M17.7 6.3l2.1-2.1"/></svg></div>
    <div class="date"><svg width="17" height="17" viewBox="0 0 24 24" fill="none" stroke="#fff" stroke-width="1.5"><rect x="2" y="4" width="18" height="17" rx="2"/><path d="M2 9h18M7 2v4M15 2v4"/><circle cx="18" cy="18" r="4" fill="#27272a"/><path d="M18 16v2h1.5"/></svg><span class="day">14</span><span class="month">July<br>2022</span></div>
    <div class="time">15:23</div>
  </header>
  <h1 class="greeting" style="top:77px"><b>Good morning</b>, today is Friday</h1>

  <div class="control" style="left:10px;top:124px">
    <svg class="icon" width="22" height="22" viewBox="0 0 24 24" fill="none" stroke="#fff" stroke-width="1.8"><circle cx="12" cy="12" r="5" fill="#fff"/><path d="M12 1v3M12 20v3M1 12h3M20 12h3M4.2 4.2l2.1 2.1M17.7 17.7l2.1 2.1M4.2 19.8l2.1-2.1M17.7 6.3l2.1-2.1"/></svg>
    <span class="title">Light</span><span class="sub">Lorem Ipsum</span>
    <div class="pill pill--off"><i class="knob"></i><span>Off</span></div>
  </div>
  <div class="control control--on" style="left:10px;top:190px">
    <svg class="icon" width="20" height="20" viewBox="0 0 24 24" fill="#fff" stroke="#fff" stroke-width="1.8"><path d="M3 9h4l5-4v14l-5-4H3z"/><path d="M15 9a4 4 0 0 1 0 6M18 6a8 8 0 0 1 0 12" fill="none"/></svg>
    <span class="title">Sound</span><span class="sub">Lorem Ipsum</span>
    <div class="pill pill--on"><span>On</span><i class="knob"></i></div>
  </div>
  <svg class="cursor" style="left:156px;top:224px" width="10" height="13" viewBox="0 0 10 13"><path d="M3 1v6L1.5 6C.5 6 .3 7 1 7.7L4 12h5V6.5L5 5.7V1c0-1-2-1-2 0z" fill="#fff" stroke="#000" stroke-width=".6"/></svg>
  <div class="slider" style="left:186px;top:186px"><div class="fill" style="height:32%"></div><div class="badge">32%</div><svg width="12" height="12" viewBox="0 0 24 24" fill="none" stroke="#fff" stroke-width="2"><path d="M4 9h4l5-4v14l-5-4H4z"/><path d="M17 10a3 3 0 0 1 0 4"/></svg></div>

  <div class="device device--on" style="left:402px;top:124px"><svg width="12" height="17" viewBox="0 0 12 17" fill="#fff"><rect x="0" y="0" width="12" height="17" rx="2"/><circle cx="6" cy="4" r="1.3" fill="#2f66f0"/><circle cx="6" cy="11" r="3.3" fill="#2f66f0"/><circle cx="6" cy="11" r="1.2" fill="#fff"/></svg><span class="label" style="top:34px">Speaker 01</span><i class="rule"></i><div class="switch"><i class="knob"></i></div></div>
  <div class="device" style="left:481px;top:124px"><svg width="12" height="17" viewBox="0 0 12 17" fill="#fff"><rect x="1" y="2" width="10" height="15" rx="2"/><ellipse cx="6" cy="2.5" rx="5" ry="1.5"/><path d="M5 8v4.5a1.2 1.2 0 1 1-.8-1.1V8l3-.7v1.3" stroke="#222" stroke-width=".9" fill="none"/></svg><span class="label" style="top:34px">Speaker 02</span><i class="rule"></i><div class="switch"><i class="knob"></i></div></div>
  <div class="device" style="left:402px;top:216px"><svg width="12" height="17" viewBox="0 0 12 17" fill="#fff"><rect x="0" y="0" width="12" height="17" rx="2"/><circle cx="6" cy="4" r="1.3" fill="#222"/><circle cx="6" cy="11" r="3.3" fill="#222"/><circle cx="6" cy="11" r="1.2" fill="#fff"/></svg><span class="label" style="top:34px">Speaker 03</span><i class="rule"></i><div class="switch"><i class="knob"></i></div></div>
  <div class="device" style="left:481px;top:216px"><svg width="12" height="17" viewBox="0 0 12 17" fill="#fff"><rect x="1" y="2" width="10" height="15" rx="2"/><ellipse cx="6" cy="2.5" rx="5" ry="1.5"/><path d="M5 8v4.5a1.2 1.2 0 1 1-.8-1.1V8l3-.7v1.3" stroke="#222" stroke-width=".9" fill="none"/></svg><span class="label" style="top:34px">Speaker 04</span><i class="rule"></i><div class="switch"><i class="knob"></i></div></div>
</section>

<!-- Bedroom sound popup -->
<section class="screen screen--bedroom" style="left:610px;top:471px">
  <div class="room-backdrop" role="img" aria-label="Blurred photo of the bedroom with a bed"></div>
  <header class="header">
    <div class="room"><svg width="15" height="11" viewBox="0 0 15 11" fill="#fff"><rect x="1.5" y="0" width="12" height="5" rx="1"/><rect x="0" y="5" width="15" height="4" rx="1"/><rect x="0.5" y="9" width="1.5" height="2"/><rect x="13" y="9" width="1.5" height="2"/></svg>Bedroom<svg width="9" height="5" viewBox="0 0 9 5"><path d="M0 0h9L4.5 5z" fill="#fff"/></svg></div>
    <div class="temp">23<sup>°</sup><svg width="17" height="17" viewBox="0 0 24 24" fill="none" stroke="#fff" stroke-width="1.8"><circle cx="12" cy="12" r="5"/><path d="M12 1v3M12 20v3M1 12h3M20 12h3M4.2 4.2l2.1 2.1M17.7 17.7l2.1 2.1M4.2 19.8l2.1-2.1M17.7 6.3l2.1-2.1"/></svg></div>
    <div class="date"><svg width="17" height="17" viewBox="0 0 24 24" fill="none" stroke="#fff" stroke-width="1.5"><rect x="2" y="4" width="18" height="17" rx="2"/><path d="M2 9h18M7 2v4M15 2v4"/><circle cx="18" cy="18" r="4" fill="#27272a"/><path d="M18 16v2h1.5"/></svg><span class="day">14</span><span class="month">July<br>2022</span></div>
    <div class="time">15:23</div>
  </header>
  <h1 class="greeting" style="top:77px"><b>Good morning</b>, today is Friday</h1>
  <div class="control" style="left:10px;top:124px">
    <svg class="icon" width="22" height="22" viewBox="0 0 24 24" fill="none" stroke="#fff" stroke-width="1.8"><circle cx="12" cy="12" r="5" fill="#fff"/><path d="M12 1v3M12 20v3M1 12h3M20 12h3M4.2 4.2l2.1 2.1M17.7 17.7l2.1 2.1M4.2 19.8l2.1-2.1M17.7 6.3l2.1-2.1"/></svg>
    <span class="title">Light</span><span class="sub">Lorem Ipsum</span>
    <div class="pill pill--off"><i class="knob"></i><span>Off</span></div>
  </div>
  <div class="device device--on" style="left:402px;top:124px"><svg width="12" height="17" viewBox="0 0 12 17" fill="#fff"><rect x="0" y="0" width="12" height="17" rx="2"/><circle cx="6" cy="4" r="1.3" fill="#2f66f0"/><circle cx="6" cy="11" r="3.3" fill="#2f66f0"/><circle cx="6" cy="11" r="1.2" fill="#fff"/></svg><span class="label" style="top:34px">Speaker 01</span><i class="rule"></i><div class="switch"><i class="knob"></i></div></div>
  <div class="device" style="left:481px;top:124px"><svg width="12" height="17" viewBox="0 0 12 17" fill="#fff"><rect x="1" y="2" width="10" height="15" rx="2"/><ellipse cx="6" cy="2.5" rx="5" ry="1.5"/></svg><span class="label" style="top:34px">Speaker 02</span><i class="rule"></i><div class="switch"><i class="knob"></i></div></div>
  <div class="device" style="left:402px;top:216px"><svg width="12" height="17" viewBox="0 0 12 17" fill="#fff"><rect x="0" y="0" width="12" height="17" rx="2"/><circle cx="6" cy="11" r="3.3" fill="#222"/></svg><span class="label" style="top:34px">Speaker 03</span><i class="rule"></i><div class="switch"><i class="knob"></i></div></div>
  <div class="device" style="left:481px;top:216px"><svg width="12" height="17" viewBox="0 0 12 17" fill="#fff"><rect x="1" y="2" width="10" height="15" rx="2"/><ellipse cx="6" cy="2.5" rx="5" ry="1.5"/></svg><span class="label" style="top:34px">Speaker 04</span><i class="rule"></i><div class="switch"><i class="knob"></i></div></div>
  <div class="dim"></div>

  <div class="control control--on" style="left:10px;top:190px">
    <svg class="icon" width="20" height="20" viewBox="0 0 24 24" fill="#fff" stroke="#fff" stroke-width="1.8"><path d="M3 9h4l5-4v14l-5-4H3z"/><path d="M15 9a4 4 0 0 1 0 6M18 6a8 8 0 0 1 0 12" fill="none"/></svg>
    <span class="title">Sound</span><span class="sub">Lorem Ipsum</span>
    <div class="pill pill--on"><span>On</span><i class="knob"></i></div>
  </div>
  <svg class="cursor" style="left:156px;top:224px" width="10" height="13" viewBox="0 0 10 13"><path d="M3 1v6L1.5 6C.5 6 .3 7 1 7.7L4 12h5V6.5L5 5.7V1c0-1-2-1-2 0z" fill="#fff" stroke="#000" stroke-width=".6"/></svg>

  <div class="popup" style="left:196px;top:144px;width:332px;height:106px">
    <h2 style="left:22px;top:20px">Play List</h2>
    <div class="select"><i class="ring"></i>Lorem Ipsum<svg width="8" height="5" viewBox="0 0 8 5"><path d="M0 0h8L4 5z" fill="#fff"/></svg></div>
  </div>
</section>

</body>
</html>
```